Safety training business card design

We need a buisness card design and logo for a small buisness that provides safety training through out the mining and civil construction industries. We provide first aid , confined space working at heights , machinery tickets, chainsaw, four wheel drive and four wheel motorbike training. We would like to use the design colors of navy blue, Fluro or lime green and white .

Industry/Entity Type

Construction

Contact Information for Business Card

Rillford Groundworks & Training , Neville Ormsby, rillford.skills@mailbox-example.net, ph 0481065374 abn 47 806 315 914

```html
<!DOCTYPE html>
<html lang="en">
<head>
<meta charset="utf-8">
<title>Rillford Groundworks &amp; Training – Business Card</title>
<link rel="stylesheet" href="https://fonts.googleapis.com/css2?family=Roboto+Condensed:wght@300;400;700&display=swap">
<style>
  :root {
    --page-bg: #d2d2d2;
    --card-yellow: #fff200;
    --navy: #1a0f5c;
    --band-start: #241c78;
    --band-mid: #2a3d9a;
    --band-end: #10a8e2;
  }
  * { margin: 0; padding: 0; box-sizing: border-box; }
  html, body {
    width: 1200px;
    height: 953px;
    overflow: hidden;
  }
  body {
    position: relative;
    background: var(--page-bg);
    font-family: "Roboto Condensed", "Arial Narrow", sans-serif;
    color: var(--navy);
  }
  .card {
    position: absolute;
    left: 376px;
    width: 446px;
    height: 269px;
    background: var(--card-yellow);
    overflow: hidden;
  }
  .card--front { top: 173px; }
  .card--back { top: 512px; }

  .card__band {
    position: absolute;
    left: 0;
    bottom: 0;
    width: 100%;
    height: 10px;
    background: linear-gradient(90deg, var(--band-start) 0%, var(--band-mid) 55%, var(--band-end) 100%);
  }

  /* Front */
  .brand {
    position: absolute;
    left: 183px;
    top: 95px;
    display: flex;
    align-items: center;
    gap: 20px;
  }
  .brand__square {
    width: 56px;
    height: 56px;
    background: var(--navy);
    flex: none;
  }
  .brand__name {
    font-weight: 700;
    font-size: 21px;
    line-height: 26px;
    letter-spacing: 0.4px;
    text-transform: uppercase;
    color: var(--navy);
  }

  /* Back */
  .contact {
    position: absolute;
    left: 82px;
    top: 66px;
  }
  .contact__company {
    font-weight: 700;
    font-size: 9.5px;
    letter-spacing: 0.2px;
    text-transform: uppercase;
  }
  .contact__name {
    margin-top: 38px;
    font-weight: 400;
    font-size: 31px;
    line-height: 1;
    letter-spacing: -0.2px;
  }
  .contact__details {
    margin-top: 21px;
    font-weight: 300;
    font-size: 16px;
    line-height: 21px;
  }
</style>
</head>
<body>
  <section class="card card--front" aria-label="Business card front">
    <div class="brand">
      <span class="brand__square" aria-hidden="true"></span>
      <p class="brand__name">Rillford<br>Groundworks<br>&amp; Training</p>
    </div>
    <div class="card__band" role="img" aria-label="Diagonal safety stripe band in navy to blue"></div>
  </section>

  <section class="card card--back" aria-label="Business card back">
    <div class="contact">
      <p class="contact__company">Rillford Groundworks &amp; Training</p>
      <h1 class="contact__name">Neville Ormsby</h1>
      <p class="contact__details">rillford.skills@mailbox-example.net<br>ph 0481065374 abn 47 806 315 914</p>
    </div>
    <div class="card__band" role="img" aria-label="Diagonal safety stripe band in navy to blue"></div>
  </section>
</body>
</html>
```